Banner

Hi,
Looking for 6 tiles. 1080 by 1080, we want the angular shapes you've used for us in the past similar to the example but bold and simple design.

Tile 1
Cedar Loop Logo (the books)
include some shapes, bold and simple

Tile 2
Text-
Let Cedar ideas grow
add some shapes

Tile 3
a diagonal line down
on one side have the Cedar Loop Logo (the books) the other side have some shapes

Tile 4
Text-
Let Cedar ideas grow
have a diagonal line down
on one side have add some shapes on the other side

Tile 5
include the rocket from the Tandem logo

Tile 6
Text-
Let Cedar ideas grow

```html
<!DOCTYPE html>
<html lang="en">
<head>
<meta charset="utf-8">
<title>Cedar Loop – social tiles</title>
<link href="https://fonts.googleapis.com/css2?family=Patrick+Hand&display=swap" rel="stylesheet">
<style>
  :root{
    --stage:#4d4d4d;
    --sky:#1bbff5;
    --sun:#ffec00;
    --leaf:#97c22b;
    --paper:#ffffff;
    --ink:#1a1a1a;
  }
  html,body{margin:0;padding:0;overflow:hidden}
  body{width:1200px;height:887px;background:var(--stage);position:relative;font-family:"Patrick Hand",cursive}
  .tile{position:absolute;width:338px;height:338px;display:block;box-shadow:0 10px 8px -6px rgba(0,0,0,.45)}
  .tile--1{left:66px;top:90px}
  .tile--2{left:432px;top:90px}
  .tile--3{left:794px;top:90px}
  .tile--4{left:66px;top:464px}
  .tile--5{left:432px;top:464px}
  .tile--6{left:796px;top:464px}
  .shape{stroke:var(--paper);stroke-width:7;stroke-linejoin:miter}
  .sky{fill:var(--sky)}
  .sun{fill:var(--sun)}
  .leaf{fill:var(--leaf)}
  .paper{fill:var(--paper)}
  .headline{font-family:"Patrick Hand",cursive;fill:var(--ink);font-size:36px;letter-spacing:1px}
  .tagline{font-family:"Patrick Hand",cursive;fill:var(--ink);font-size:21px;letter-spacing:.5px}
  .brand{font-family:"Patrick Hand",cursive;fill:var(--ink);font-size:19px}
  .brand-dot{fill:var(--paper);stroke:var(--sky);stroke-width:8}
  .brand-dot--plain{fill:var(--paper)}
</style>
</head>
<body>

<!-- Tile 1 : brand cover -->
<svg class="tile tile--1" viewBox="0 0 422 422" aria-label="Cedar Loop cover tile">
  <rect class="paper" width="422" height="422"/>
  <polygon class="sky" points="0,0 122,0 0,122"/>
  <polygon class="sun" points="422,15 285,153 422,290"/>
  <polygon class="leaf" points="0,288 135,422 0,422"/>
  <polygon class="sky" points="200,422 329,293 422,386 422,422"/>
  <circle class="brand-dot" cx="210" cy="133" r="36"/>
  <text class="brand" x="210" y="196" text-anchor="middle">Brightwell</text>
  <text class="headline" x="210" y="244" text-anchor="middle">Cedar Loop</text>
  <text class="headline" x="210" y="278" text-anchor="middle">Room</text>
</svg>

<!-- Tile 2 : tagline -->
<svg class="tile tile--2" viewBox="0 0 422 422" aria-label="Tagline tile">
  <rect class="sun" width="422" height="422"/>
  <polygon class="shape sky" points="293,-5 427,-5 427,128"/>
  <polygon class="shape leaf" points="-5,218 112,358 50,427 -5,427"/>
  <polygon class="shape sky" points="112,358 427,358 427,427 50,427"/>
  <text class="tagline" x="268" y="395" text-anchor="middle">“Let Cedar ideas grow”</text>
</svg>

<!-- Tile 3 : diagonal with brand -->
<svg class="tile tile--3" viewBox="0 0 422 422" aria-label="Diagonal brand tile">
  <rect class="sun" width="422" height="422"/>
  <polygon class="shape sky" points="132,-5 422,-5 279,150"/>
  <polygon class="shape sky" points="-5,198 229,427 -5,427"/>
  <circle class="brand-dot" cx="64" cy="335" r="34"/>
  <text class="brand" x="64" y="395" text-anchor="middle">Brightwell</text>
</svg>

<!-- Tile 4 : tagline with diagonal -->
<svg class="tile tile--4" viewBox="0 0 422 422" aria-label="Tagline diagonal tile">
  <rect class="sun" width="422" height="422"/>
  <polygon class="shape leaf" points="250,-5 427,-5 427,172 295,52"/>
  <polygon class="shape sky" points="-5,-5 250,-5 295,52 -5,52"/>
  <polygon class="shape sky" points="-5,427 145,272 300,427"/>
  <text class="tagline" x="20" y="33">“Let Cedar ideas grow”</text>
</svg>

<!-- Tile 5 : partner corner -->
<svg class="tile tile--5" viewBox="0 0 422 422" aria-label="Partner tile">
  <rect class="sun" width="422" height="422"/>
  <polygon class="shape sky" points="-5,-5 220,-5 60,165 -5,108"/>
  <polygon class="shape leaf" points="-5,368 255,368 205,427 -5,427"/>
  <polygon class="shape sky" points="427,205 427,427 205,427"/>
  <circle class="brand-dot" cx="62" cy="53" r="26"/>
  <text class="brand" x="62" y="100" text-anchor="middle">Brightwell</text>
  <circle class="brand-dot--plain" cx="355" cy="335" r="16"/>
  <text class="tagline" x="355" y="385" text-anchor="middle">Tandem</text>
</svg>

<!-- Tile 6 : tagline with partner -->
<svg class="tile tile--6" viewBox="0 0 422 422" aria-label="Tagline partner tile">
  <rect class="sun" width="422" height="422"/>
  <polygon class="shape sky" points="322,-5 427,-5 427,200 255,67"/>
  <polygon class="shape leaf" points="-5,-5 322,-5 255,67 -5,67"/>
  <polygon class="shape sky" points="-5,427 103,315 210,427"/>
  <text class="tagline" x="25" y="41">“Let Cedar ideas grow”</text>
  <circle class="brand-dot--plain" cx="350" cy="38" r="16"/>
  <text class="tagline" x="350" y="88" text-anchor="middle">Tandem</text>
</svg>

</body>
</html>
```